" buscamos elaborar produtos saudáveis, isentos de glúten, lactose e açúcar. E utilizando ingredientes benéficos a nossa saúde, como fibra e gorduras boas (insaturadas). "

```html
<!DOCTYPE html>
<html lang="pt-BR">
<head>
<meta charset="UTF-8">
<title>Cartão Fidelidade — Sementes Vivas</title>
<link rel="stylesheet" href="https://fonts.googleapis.com/css2?family=Open+Sans:wght@400;600;700&display=swap">
<style>
  :root {
    --page-bg: #ecebe8;
    --card-bg: #ffffff;
    --brand-green: #6f9a1c;
    --brand-green-dark: #5b8214;
    --accent-orange: #e98a2a;
    --leaf-tint: #eef0ea;
    --slot-white: #ffffff;
  }
  * { box-sizing: border-box; margin: 0; padding: 0; }
  html, body {
    width: 1200px;
    height: 1200px;
    overflow: hidden;
    background: var(--page-bg);
    font-family: "Open Sans", Arial, sans-serif;
  }
  .canvas {
    position: relative;
    width: 1200px;
    height: 1200px;
  }
  .loyalty-card {
    position: absolute;
    left: 100px;
    top: 285px;
    width: 1000px;
    height: 630px;
    background: var(--card-bg);
    border-radius: 28px;
    overflow: hidden;
    box-shadow: 0 10px 30px rgba(0,0,0,0.12);
  }
  .leaf-backdrop {
    position: absolute;
    left: 0;
    top: 0;
    width: 560px;
    height: 630px;
    background: radial-gradient(ellipse at 30% 25%, var(--leaf-tint) 0%, rgba(238,240,234,0.5) 45%, rgba(255,255,255,0) 75%);
  }
  .card-title {
    position: absolute;
    left: 62px;
    top: 48px;
    font-size: 40px;
    font-weight: 600;
    color: var(--accent-orange);
    letter-spacing: 0.5px;
  }
  .brand {
    position: absolute;
    right: 58px;
    top: 40px;
    display: flex;
    flex-direction: column;
    align-items: center;
    gap: 8px;
  }
  .brand-dot {
    width: 96px;
    height: 96px;
    border-radius: 50%;
    background: var(--accent-orange);
  }
  .brand-name {
    font-size: 44px;
    font-weight: 600;
    color: var(--brand-green);
    line-height: 1;
  }
  .stamp-band {
    position: absolute;
    left: 0;
    top: 212px;
    width: 100%;
    height: 262px;
    background: var(--brand-green);
  }
  .stamp-slots {
    position: absolute;
    left: 40px;
    right: 40px;
    top: 24px;
    display: flex;
    justify-content: space-between;
  }
  .stamp-slot {
    width: 162px;
    height: 150px;
    background: var(--slot-white);
    border-radius: 16px;
  }
  .validity {
    position: absolute;
    left: 200px;
    top: 196px;
    width: 470px;
    height: 44px;
    display: flex;
    align-items: center;
  }
  .validity-label {
    font-size: 26px;
    font-weight: 700;
    color: #ffffff;
    width: 130px;
  }
  .validity-field {
    flex: 1;
    height: 36px;
    background: var(--slot-white);
    border-radius: 4px;
    display: flex;
    align-items: center;
    justify-content: space-around;
    padding: 0 60px;
    font-size: 24px;
    color: var(--brand-green-dark);
  }
  .website {
    position: absolute;
    left: 0;
    width: 100%;
    top: 520px;
    text-align: center;
    font-size: 36px;
    font-weight: 700;
    color: var(--brand-green);
  }
</style>
</head>
<body>
  <div class="canvas">
    <div class="loyalty-card">
      <div class="leaf-backdrop" role="img" aria-label="Folhagem decorativa clara ao fundo"></div>
      <div class="card-title">Cartão Fidelidade</div>
      <div class="brand">
        <div class="brand-dot"></div>
        <div class="brand-name">Sementes Vivas</div>
      </div>
      <div class="stamp-band">
        <div class="stamp-slots">
          <div class="stamp-slot"></div>
          <div class="stamp-slot"></div>
          <div class="stamp-slot"></div>
          <div class="stamp-slot"></div>
          <div class="stamp-slot"></div>
        </div>
        <div class="validity">
          <span class="validity-label">Validade</span>
          <span class="validity-field"><span>/</span><span>/</span></span>
        </div>
      </div>
      <div class="website">www.sementesvivas.com</div>
    </div>
  </div>
</body>
</html>
```